Sale Hang Tag

Design a bright, cheerful, compelling, call to action sale tag for a lighting showroom. The tag will be used to move older or discontinued product at a really good price. Upscale, friendly, neighbor store. Size should be no larger than 4 by 6 inches.

Industry/Entity Type

Call

```html
<!DOCTYPE html>
<html lang="en">
<head>
<meta charset="UTF-8">
<title>Sale Hang Tag</title>
<link rel="stylesheet" href="https://fonts.googleapis.com/css2?family=Roboto+Slab:wght@700;800;900&display=swap">
<style>
  :root {
    --backdrop: #e9e9e9;
    --tag-pink: #ff1a7c;
    --tag-pink-deep: #f0126f;
    --tag-pink-soft: #ff4a96;
    --ring-tint: rgba(255, 120, 180, 0.16);
    --badge-black: #050505;
    --hole-grey: #8f8f8f;
  }
  * { margin: 0; padding: 0; box-sizing: border-box; }
  html, body {
    width: 1200px;
    height: 900px;
    overflow: hidden;
    background: var(--backdrop);
  }
  .canvas {
    position: relative;
    width: 1200px;
    height: 900px;
  }
  .hang-tag {
    position: absolute;
    left: 320px;
    top: 50px;
    width: 560px;
    height: 800px;
    border-radius: 280px;
    overflow: hidden;
    background: var(--tag-pink);
  }
  .confetti-field {
    position: absolute;
    inset: 0;
    background:
      radial-gradient(ellipse at 30% 25%, var(--tag-pink-soft) 0, transparent 55%),
      radial-gradient(ellipse at 72% 78%, var(--tag-pink-soft) 0, transparent 50%),
      linear-gradient(160deg, var(--tag-pink) 0%, var(--tag-pink-deep) 50%, var(--tag-pink) 100%);
  }
  .halo-ring {
    position: absolute;
    left: 50%;
    top: 430px;
    border-radius: 50%;
    border: 30px solid var(--ring-tint);
    transform: translate(-50%, -50%);
  }
  .halo-ring--inner { width: 390px; height: 390px; }
  .halo-ring--middle { width: 500px; height: 500px; }
  .halo-ring--outer { width: 610px; height: 610px; }
  .string-hole {
    position: absolute;
    left: 50%;
    top: 46px;
    width: 44px;
    height: 44px;
    margin-left: -22px;
    border-radius: 50%;
    background: var(--hole-grey);
  }
  .sale-badge {
    position: absolute;
    left: 50%;
    top: 430px;
    width: 300px;
    height: 300px;
    border-radius: 50%;
    background: var(--badge-black);
    transform: translate(-50%, -50%);
    display: flex;
    align-items: center;
    justify-content: center;
  }
  .sale-badge__word {
    font-family: "Roboto Slab", "Rockwell", serif;
    font-weight: 800;
    font-size: 78px;
    line-height: 1;
    letter-spacing: 2px;
    white-space: nowrap;
    color: var(--tag-pink);
    transform: rotate(-33deg);
  }
</style>
</head>
<body>
  <main class="canvas">
    <article class="hang-tag">
      <div class="confetti-field" role="img" aria-label="Festive pink confetti and streamers scattered across the tag"></div>
      <div class="halo-ring halo-ring--outer"></div>
      <div class="halo-ring halo-ring--middle"></div>
      <div class="halo-ring halo-ring--inner"></div>
      <div class="string-hole"></div>
      <div class="sale-badge">
        <h1 class="sale-badge__word">SALE!</h1>
      </div>
    </article>
  </main>
</body>
</html>
```